Verpackungsdesign für Nahrungsergänzungsmittel
Zielgruppe
Wir sind eine Firma für Nahrungsergänzungsmittel und suchen für unser neues Produkt ein Ansprechendes Etikett für die Dose. Das Produkt: GLANZ KRAFT KERN
Aufgabenstellung
Deckel: weiß, geriffelt
Etikettengröße: 145 x 50 mm
Folgender Inhalt muss auf die Dose: Siehe Screenshot 0012
Außerdem soll unser Logo drauf: Siehe Bild waldquellig.734.png
Bitte an folgenden Beispielen orientieren:
https://www.kaufhalle-beispiel.example/Lumetra-Glanz-Kraft-Hochdosiert-Vitalkomplex/dp/X00000000Q

```html
<!DOCTYPE html>
<html lang="de">
<head>
<meta charset="utf-8">
<title>Waldquellig – Glanz Kraft Kern Etikett</title>
<link href="https://fonts.googleapis.com/css2?family=Exo+2:wght@300;400;500;800&display=swap" rel="stylesheet">
<style>
  :root {
    --backdrop: #eceef3;
    --label-white: #ffffff;
    --ink: #222222;
    --ink-soft: #3a3a3a;
    --leaf-green: #86c745;
    --band-text: #ffffff;
  }
  * { box-sizing: border-box; margin: 0; padding: 0; }
  html, body {
    width: 1132px; height: 1200px; overflow: hidden;
    background: var(--backdrop);
    font-family: "Exo 2", sans-serif;
  }
  .label {
    position: absolute; left: 256px; top: 190px;
    width: 620px; height: 820px;
    background: var(--label-white);
    box-shadow: 0 6px 24px rgba(0,0,0,0.06);
  }
  .brand {
    position: absolute; left: 0; right: 0; top: 200px;
    display: flex; justify-content: center; align-items: center; gap: 16px;
  }
  .brand-dot {
    width: 26px; height: 26px; border-radius: 50%;
    background: var(--leaf-green);
  }
  .brand-name {
    font-weight: 400; font-size: 44px; letter-spacing: 1px;
    color: var(--ink-soft);
  }
  .product-title {
    position: absolute; left: 0; right: 0; top: 305px;
    text-align: center;
    font-weight: 800; font-size: 80px; line-height: 96px;
    color: var(--ink);
    letter-spacing: 1px;
  }
  .divider {
    position: absolute; left: 100px; width: 380px; top: 538px;
    height: 2px; background: var(--ink);
  }
  .actives {
    position: absolute; left: 170px; top: 555px;
    font-weight: 500; font-size: 40px; letter-spacing: 2px;
    color: var(--ink);
  }
  .category {
    position: absolute; left: 100px; top: 635px;
    font-weight: 300; font-size: 29px; letter-spacing: 1px;
    color: var(--ink-soft);
  }
  .count-band {
    position: absolute; left: 0; right: 0; top: 685px; height: 72px;
    background: var(--leaf-green);
    display: flex; align-items: center; padding-left: 120px;
  }
  .count-band span {
    font-weight: 400; font-size: 40px; letter-spacing: 4px;
    color: var(--band-text);
  }
</style>
</head>
<body>
  <div class="label">
    <div class="brand">
      <div class="brand-dot"></div>
      <div class="brand-name">WALDQUELLIG</div>
    </div>
    <h1 class="product-title">GLANZ KRAFT<br>KERN</h1>
    <div class="divider"></div>
    <div class="actives">BIOTIN + ZINK</div>
    <div class="category">Nahrungsergänzungsmittel</div>
    <div class="count-band"><span>60 KAPSELN</span></div>
  </div>
</body>
</html>
```